Letter Head for accounting firm

We need letter head designed using our attached logo.

We also need the following information on the letterhead:

482 E Mill Rd. Danvers, OH 43762

HarborLedgerLtd.com

1-855-613-2907

Contact Information for Business Card

Use logo

Colors

Designer to choose colors to be used in the design.

Requirements
Must have
• Business Card - Should also have name and title - email address

```html
<!DOCTYPE html>
<html lang="en">
<head>
<meta charset="utf-8">
<title>Harbor Ledger Group LTD – Letterhead</title>
<link rel="stylesheet" href="https://fonts.googleapis.com/css2?family=Lato:wght@400;700&family=Yellowtail&display=swap">
<style>
  :root {
    --brand-blue: #1479c4;
    --ink: #4a4a4a;
    --ink-dark: #222222;
    --rule-dark: #2b2b2b;
    --paper: #ffffff;
    --paper-shade: #f1f1f1;
    --divider: #bdbdbd;
  }
  * { margin: 0; padding: 0; box-sizing: border-box; }
  html, body { width: 996px; height: 1200px; overflow: hidden; }
  body {
    font-family: "Lato", Arial, sans-serif;
    background: linear-gradient(160deg, var(--paper) 40%, var(--paper-shade) 100%);
    position: relative;
    color: var(--ink);
  }
  .brand {
    position: absolute;
    left: 31px;
    top: 40px;
    width: 221px;
    text-align: center;
  }
  .brand-mark {
    display: block;
    width: 58px;
    height: 58px;
    margin: 0 auto 14px;
    background: var(--brand-blue);
  }
  .brand-name {
    font-weight: 700;
    font-size: 19px;
    line-height: 1.2;
    color: var(--brand-blue);
    letter-spacing: 0.2px;
  }
  .contact {
    position: absolute;
    left: 698px;
    top: 47px;
    height: 60px;
    padding-left: 20px;
    border-left: 1px solid var(--divider);
    font-size: 18px;
    color: var(--ink-dark);
  }
  .contact-row {
    display: flex;
    align-items: center;
    gap: 6px;
    height: 28px;
  }
  .contact-row svg { width: 14px; height: 14px; flex: none; }
  .letter {
    position: absolute;
    left: 86px;
    top: 296px;
    width: 826px;
  }
  .salutation {
    font-weight: 700;
    font-size: 18px;
    color: var(--brand-blue);
    margin-bottom: 24px;
  }
  .letter-body p {
    font-size: 18.3px;
    line-height: 27px;
    margin-bottom: 21px;
    text-align: justify;
  }
  .closing {
    font-size: 21px;
    color: var(--ink-dark);
    margin-top: 33px;
  }
  .signature {
    font-family: "Yellowtail", cursive;
    font-size: 42px;
    color: var(--brand-blue);
    line-height: 1.2;
  }
  .footer-rule {
    position: absolute;
    top: 1147px;
    left: 0;
    right: 0;
    height: 5px;
  }
  .footer-rule .rule-dark {
    position: absolute; left: 0; width: 47px; top: 1px; height: 4px;
    background: var(--rule-dark);
  }
  .footer-rule .rule-blue {
    position: absolute; left: 52px; right: 0; top: 0; height: 4px;
    background: var(--brand-blue);
  }
  .address {
    position: absolute;
    top: 1160px;
    left: 0;
    right: 0;
    display: flex;
    justify-content: center;
    align-items: center;
    gap: 7px;
    font-size: 18px;
    color: var(--ink-dark);
  }
  .address svg { width: 13px; height: 18px; }
</style>
</head>
<body>
  <header>
    <div class="brand">
      <span class="brand-mark" aria-hidden="true"></span>
      <div class="brand-name">HARBOR LEDGER GROUP<br>LTD</div>
    </div>
    <div class="contact">
      <div class="contact-row">
        <svg viewBox="0 0 16 16" aria-hidden="true"><circle cx="8" cy="8" r="7" fill="none" stroke="#1479c4" stroke-width="1.5"/><path d="M5.5 4.5l1.5 0 .8 2-1 .8a5 5 0 0 0 2 2l.8-1 2 .8v1.5c-3.5.3-6.5-2.6-6.1-6.1z" fill="#1479c4"/></svg>
        <span>1-855-613-2907</span>
      </div>
      <div class="contact-row">
        <svg viewBox="0 0 16 16" aria-hidden="true"><g fill="none" stroke="#1479c4" stroke-width="1.3"><circle cx="8" cy="8" r="6.5"/><ellipse cx="8" cy="8" rx="3" ry="6.5"/><path d="M1.5 8h13M2.5 4.8h11M2.5 11.2h11"/></g></svg>
        <span>www.harborledgerltd.com</span>
      </div>
    </div>
  </header>

  <main class="letter">
    <p class="salutation">Dear Mr. Lorem,</p>
    <div class="letter-body">
      <p>Lorem ipsum dolor sit amet, consectetuer adipiscing elit, sed diam nonummy nibh euismod tincidunt ut laoreet dolore magna aliquam erat volutpat. Ut wisi enim ad minim veniam, quis nostrud exerci tation ullamcorper suscipit lobortis nisl ut aliquip ex ea commodo consequat. Duis autem vel eum iriure dolor in hendiusto odio dignissim qui blandit praesent luptatum zzril delenit augue duis dolore te feugait nulla facilisi.</p>
      <p>Lorem ipsum dolor sit amet, consectetuer adipiscing elit, sed diam nonummy nibh euismod tincidunt ut laoreet dolore magna aliquam erat volutpat. Ut wisi enim ad minim veniam, quis nostrud exerci tation ullamcorper suscipit lobortis nisl ut aliquip ex ea commodo consequat. Duis autem vel eum iriure dolor in hendiusto odio dignissim qui blandit praesent luptatum zzril delenit augue duis dolore te feugait nulla facilisi.</p>
      <p>Lorem ipsum dolor sit amet, consectetuer adipiscing elit, sed diam nonummy nibh euismod tincidunt ut laoreet dolore magna aliquam erat volutpat. Ut wisi enim ad minim veniam, quis nostrud exerci tation ullamcorper suscipit lobortis nisl ut aliquip ex ea commodo consequat. Duis autem vel eum iriure dolor in hendiusto odio dignissim qui blandit praesent luptatum zzril delenit augue duis dolore te feugait nulla facilisi.</p>
    </div>
    <p class="closing">Sincerely Your,</p>
    <p class="signature">Your Name</p>
  </main>

  <footer>
    <div class="footer-rule" aria-hidden="true"><span class="rule-dark"></span><span class="rule-blue"></span></div>
    <div class="address">
      <svg viewBox="0 0 12 17" aria-hidden="true"><path d="M6 0a6 6 0 0 0-6 6c0 4.5 6 11 6 11s6-6.5 6-11a6 6 0 0 0-6-6zm0 8.5a2.5 2.5 0 1 1 0-5 2.5 2.5 0 0 1 0 5z" fill="#1479c4"/></svg>
      <span>482 E Mill Rd. Danvers, OH 43762</span>
    </div>
  </footer>
</body>
</html>
```